Custom Seed Packet design for Flower Farm

We need a design for our seeds packets.
The design will be a kind of "fill in the blanks" as we need the design to be adaptable for multiple varieties of seed. We will be using the design for a rubber stamp.
Our seed packets are 90x90mm in size.
Black logo only. No colour required.
A vintage botanical influence is desired.
Will need to include the following info,
"Lantern Wick Co logo" , "Seeds", "Plant Type", "Variety", "Harvested"

```html
<!DOCTYPE html>
<html lang="en">
<head>
<meta charset="utf-8">
<title>Seed Packet – Lantern Wick Co. Flower Farm</title>
<link rel="stylesheet" href="https://fonts.googleapis.com/css2?family=Cormorant+Garamond:wght@500&family=Pinyon+Script&display=swap">
<style>
  :root {
    --kraft: #d3c09d;
    --kraft-edge: #c7b28b;
    --ink: #1c1915;
  }
  * { margin: 0; padding: 0; box-sizing: border-box; }
  html, body {
    width: 1122px;
    height: 1200px;
    overflow: hidden;
    background: var(--kraft);
  }
  .packet-face {
    position: relative;
    width: 1122px;
    height: 1200px;
    background: radial-gradient(ellipse at 50% 45%, var(--kraft) 60%, var(--kraft-edge) 100%);
  }
  .frame {
    position: absolute;
    inset: 0;
  }
  .seeds-title {
    position: absolute;
    top: 224px;
    left: 0;
    width: 100%;
    text-align: center;
    font-family: "Cormorant Garamond", serif;
    font-weight: 500;
    font-size: 84px;
    letter-spacing: 0.42em;
    padding-left: 0.42em;
    color: var(--ink);
    line-height: 1;
  }
  .brand-name {
    position: absolute;
    top: 500px;
    left: 0;
    width: 100%;
    text-align: center;
    font-family: "Cormorant Garamond", serif;
    font-weight: 500;
    font-size: 52px;
    color: var(--ink);
    line-height: 1.15;
  }
  .fields {
    position: absolute;
    left: 240px;
    width: 641px;
    top: 782px;
    list-style: none;
  }
  .field {
    display: flex;
    align-items: flex-end;
    height: 67px;
    gap: 14px;
  }
  .field-label {
    font-family: "Pinyon Script", cursive;
    font-size: 30px;
    color: var(--ink);
    white-space: nowrap;
    line-height: 1;
  }
  .field-line {
    flex: 1;
    border-bottom: 1.5px solid var(--ink);
    margin-bottom: 4px;
  }
</style>
</head>
<body>
  <main class="packet-face">
    <svg class="frame" width="1122" height="1200" viewBox="0 0 1122 1200" aria-hidden="true">
      <g fill="var(--ink)">
        <!-- top rule band -->
        <rect x="120" y="160" width="882" height="4"/>
        <rect x="120" y="179" width="882" height="3.5"/>
        <rect x="120" y="196" width="882" height="2.5"/>
        <!-- side rules -->
        <rect x="121" y="254" width="4" height="686"/>
        <rect x="145" y="347" width="4" height="599"/>
        <rect x="997" y="254" width="4" height="686"/>
        <rect x="972" y="347" width="4" height="599"/>
        <!-- bottom rule band -->
        <rect x="120" y="998" width="882" height="2.5"/>
        <rect x="120" y="1015" width="882" height="3.5"/>
        <rect x="120" y="1033" width="882" height="4"/>
      </g>
    </svg>

    <h1 class="seeds-title">SEEDS</h1>

    <p class="brand-name">Lantern Wick Co.<br>Flower Farm</p>

    <ul class="fields">
      <li class="field"><span class="field-label">Plant Type</span><span class="field-line"></span></li>
      <li class="field"><span class="field-label">Variety</span><span class="field-line"></span></li>
      <li class="field"><span class="field-label">Harvested</span><span class="field-line"></span></li>
    </ul>
  </main>
</body>
</html>
```